Quorlify Business Card

We require a stunning business card for Quorlify - a new digital marketing agency. The logo provided was designed by a graphic designer here on Artboxly.

www.quorlify-example.com - "Get more sales online"

What we do:
The business delivers website optimisation (Web design, social media strategy, digital strategies, SEO, PPC, conversion optimisation, email marketing) to get businesses more sales online.

The card must match the brand style which can be found on this website template:

http://layoutmarket.example/item/brightline-adaptive-versatile-layout/full_screen_preview/9137462

It must have 'wow' factor so that you'll never forget Quorlify - We're open to any materials, textures you think will work.

We don't want a boring run of the mill design - I can knock that up in Photoshop myself or use a template solution. It should be timeless and only need replacing should the contact details change.

The design should be eye catching, future proof, exceptionally chic, classy and oozing authority and confidence. Quorlify services must not look cheap.

Here's some brilliant designs to point you in the right direction:

http://tidyprints.example/30-remarkable-calling-cards/

The spec is for double sided, but we're open to your ideas. If it's going on an opaque or see through card, then of course a single side is preferable. Using creativity and thought on the medium for the card - shape - texture is desirable.

The strapline for the business is "Get more business online" please submit with / without strapline.
Updates

Please only submit your best 1-3 designs initially.

Target Market(s)

Business 2 Business - Local SMEs
Local professionals - Doctors, Dentists, Financials, Bespoke Retailers, Property companies - anyone with a decent budget to spend on digital marketing services and a high margin product or service to sell.

Industry/Entity Type

Graphic Designer

Requirements
Must have
• Text:
• name: Tom Vandlow
• position Digital Marketing Director
• mobile 07951 238 604
• website www.quorlify-example.com
Nice to have
• Check See http://tidyprints.example/30-remarkable-calling-cards/ for ideas.
• LinkedIn and Twitter usernames if there is space and it works on the design.

```html
<!DOCTYPE html>
<html lang="en">
<head>
<meta charset="utf-8">
<title>Quorlify Business Card</title>
<link href="https://fonts.googleapis.com/css2?family=Open+Sans:wght@400;600;700&display=swap" rel="stylesheet">
<style>
  :root {
    --backdrop: #d9d9d9;
    --brand-navy: #0c3d51;
    --brand-red: #ee3524;
    --card-white: #ffffff;
    --text-navy: #0c3d51;
  }
  * { box-sizing: border-box; margin: 0; padding: 0; }
  html, body {
    width: 1200px; height: 900px; overflow: hidden;
    background: var(--backdrop);
    font-family: "Open Sans", Arial, sans-serif;
  }
  .canvas { position: relative; width: 1200px; height: 900px; }

  /* Back of card */
  .card-back {
    position: absolute; left: 113px; top: 135px;
    width: 340px; height: 605px;
    background: var(--brand-navy);
    overflow: hidden;
  }
  .card-back__disc {
    position: absolute; left: 74px; top: 169px;
    width: 220px; height: 220px; border-radius: 50%;
    background: var(--brand-red);
    display: flex; align-items: center; justify-content: center;
  }
  .card-back__url {
    color: var(--card-white); font-size: 17px; font-weight: 400;
    white-space: nowrap;
  }

  /* Front of card */
  .card-front {
    position: absolute; left: 497px; top: 399px;
    width: 605px; height: 341px;
    background: var(--card-white);
    overflow: hidden;
  }
  .brand {
    position: absolute; left: 22px; top: 18px;
    display: flex; align-items: center; gap: 12px;
  }
  .brand__dot {
    width: 30px; height: 30px; border-radius: 50%;
    background: var(--brand-red);
  }
  .brand__name {
    color: var(--text-navy); font-size: 56px; font-weight: 600;
    line-height: 1; letter-spacing: -0.5px;
  }
  .holder { position: absolute; left: 22px; top: 166px; }
  .holder__name {
    color: var(--brand-red); font-size: 20px; font-weight: 700; line-height: 1.1;
  }
  .holder__role {
    color: var(--text-navy); font-size: 13px; font-weight: 400; margin-top: 5px;
  }
  .contacts {
    position: absolute; left: 22px; top: 230px;
    list-style: none;
  }
  .contacts__item {
    display: flex; align-items: center; gap: 14px;
    height: 22.6px; color: var(--text-navy); font-size: 13.5px;
  }
  .contacts__icon { width: 18px; height: 18px; flex: none; }
  .card-front__arc { position: absolute; inset: 0; }
  .card-front__tagline {
    fill: var(--card-white); font-size: 18.5px; font-weight: 400;
    font-family: "Open Sans", Arial, sans-serif;
  }
</style>
</head>
<body>
<main class="canvas">

  <section class="card-back" aria-label="Card back">
    <div class="card-back__disc">
      <span class="card-back__url">www.quorlify-example.com</span>
    </div>
  </section>

  <section class="card-front" aria-label="Card front">
    <div class="brand">
      <span class="brand__dot"></span>
      <span class="brand__name">Quorlify</span>
    </div>

    <div class="holder">
      <p class="holder__name">SAM PELLOW</p>
      <p class="holder__role">Director</p>
    </div>

    <ul class="contacts">
      <li class="contacts__item">
        <svg class="contacts__icon" viewBox="0 0 18 18"><circle cx="9" cy="9" r="9" fill="var(--brand-red)"/><path d="M6 4.5c.6-.3 1 0 1.3.6l.6 1.4c.2.5 0 .9-.4 1.2l-.4.3c.4 1 1.4 2 2.4 2.4l.3-.4c.3-.4.7-.6 1.2-.4l1.4.6c.6.3.9.7.6 1.3-.4 1-1.3 1.5-2.3 1.2C8.300 12.100 5.900 9.700 5.300 7.300 5 6.200 5.300 5 6 4.500z" fill="#fff"/></svg>
        <span>0161 482 907</span>
      </li>
      <li class="contacts__item">
        <svg class="contacts__icon" viewBox="0 0 18 18"><circle cx="9" cy="9" r="9" fill="var(--brand-red)"/><rect x="6" y="3.5" width="6" height="11" rx="1.2" fill="#fff"/><rect x="7" y="5" width="4" height="7" fill="var(--brand-red)"/></svg>
        <span>07951 238 604</span>
      </li>
      <li class="contacts__item">
        <svg class="contacts__icon" viewBox="0 0 18 18"><circle cx="9" cy="9" r="9" fill="var(--brand-red)"/><rect x="4" y="5.5" width="10" height="7" fill="#fff"/><path d="M4 5.5l5 4 5-4" fill="none" stroke="var(--brand-red)" stroke-width="1"/></svg>
        <span>sampellow@quorlify-example.com</span>
      </li>
      <li class="contacts__item">
        <svg class="contacts__icon" viewBox="0 0 18 18"><circle cx="9" cy="9" r="8" fill="none" stroke="var(--brand-red)" stroke-width="1.5"/><ellipse cx="9" cy="9" rx="3.5" ry="8" fill="none" stroke="var(--brand-red)" stroke-width="1.2"/><path d="M1 9h16M2.500 5h13M2.500 13h13" stroke="var(--brand-red)" stroke-width="1.2"/></svg>
        <span>www.quorlify-example.com</span>
      </li>
    </ul>

    <svg class="card-front__arc" viewBox="0 0 605 341" width="605" height="341">
      <path d="M354 341 A251 251 0 0 1 605 90 L605 234 A107 107 0 0 0 498 341 Z" fill="var(--brand-red)"/>
      <path id="taglinePath" d="M425 341 A180 180 0 0 1 605 161" fill="none"/>
      <text class="card-front__tagline">
        <textPath href="#taglinePath" startOffset="14%">Get more sales online</textPath>
      </text>
    </svg>
  </section>

</main>
</body>
</html>
```